Business Card and Stationery for Brokerage & Consulting Co.
Amber Ridge Associates, Brokerage & Consulting for the Baking Industry
Business Card and Stationery for Brokerage & Consulting Co. - Food
Creative Brief
Professional
Derek Halvorsen
Partner / Business Development
4219 W. Birchmont Ave. Long Beach, CA 90714
derek@amberridgeassociates.com

```html
<!DOCTYPE html>
<html lang="en">
<head>
<meta charset="utf-8">
<title>Amber Ridge Associates – Business Card</title>
<link href="https://fonts.googleapis.com/css2?family=Open+Sans:wght@400;600&family=Lora:ital,wght@1,400&display=swap" rel="stylesheet">
<style>
  :root {
    --stage: #e6e6e4;
    --paper: #f7f7f5;
    --edge: #d9d9d6;
    --maroon: #6e1a1f;
    --olive: #5e7a1e;
    --ink: #333333;
  }
  * { box-sizing: border-box; margin: 0; padding: 0; }
  html, body { width: 1200px; height: 874px; overflow: hidden; }
  body {
    background: var(--stage);
    font-family: "Open Sans", Arial, sans-serif;
    display: flex;
    align-items: center;
    justify-content: center;
    gap: 60px;
  }
  .card {
    position: relative;
    width: 520px;
    height: 298px;
    background: var(--paper);
    border: 1px solid var(--edge);
    border-radius: 16px;
    box-shadow: 0 6px 18px rgba(0,0,0,.12);
  }
  .brand {
    display: flex;
    align-items: center;
    gap: 12px;
  }
  .brand-mark {
    width: 38px; height: 38px;
    border-radius: 50%;
    background: var(--maroon);
    flex: none;
  }
  .brand-name {
    font-family: "Open Sans", Arial, sans-serif;
    font-weight: 600;
    color: var(--olive);
    line-height: 1.15;
  }
  .card-front .brand {
    position: absolute;
    left: 50%; top: 50%;
    transform: translate(-50%, -50%);
  }
  .card-front .brand-name { font-size: 24px; }
  .card-back .brand {
    position: absolute;
    left: 34px; top: 108px;
  }
  .card-back .brand-mark { width: 30px; height: 30px; }
  .card-back .brand-name { font-size: 17px; }
  .person {
    position: absolute;
    right: 36px; top: 48px;
    text-align: right;
  }
  .person-name {
    font-family: "Lora", Georgia, serif;
    font-style: italic;
    font-size: 19px;
    color: var(--maroon);
  }
  .person-title {
    margin-top: 4px;
    font-size: 9.5px;
    color: var(--olive);
    font-style: normal;
  }
  .divider {
    position: absolute;
    left: 34px; right: 36px; top: 100px;
    height: 1px;
    background: var(--edge);
  }
  .contact {
    position: absolute;
    left: 34px; bottom: 28px;
    list-style: none;
    font-size: 11px;
    color: var(--ink);
    line-height: 1.55;
  }
  .contact li { display: flex; align-items: flex-start; gap: 8px; }
  .contact svg { width: 11px; height: 11px; margin-top: 3px; fill: var(--maroon); flex: none; }
  .contact .indent { padding-left: 19px; }
</style>
</head>
<body>
  <section class="card card-front" aria-label="Card front">
    <div class="brand">
      <span class="brand-mark"></span>
      <span class="brand-name">Amber Ridge Associates</span>
    </div>
  </section>

  <section class="card card-back" aria-label="Card back">
    <div class="person">
      <p class="person-name">Derek Halvorsen</p>
      <p class="person-title">Partner / Business Development</p>
    </div>
    <div class="brand">
      <span class="brand-mark"></span>
      <span class="brand-name">Amber Ridge Associates</span>
    </div>
    <ul class="contact">
      <li>
        <svg viewBox="0 0 12 12"><path d="M6 1 L11 6 H9.5 V11 H7 V8 H5 V11 H2.5 V6 H1 Z"/></svg>
        <span>4219 W. Birchmont Ave.</span>
      </li>
      <li class="indent">Long Beach, CA 90714</li>
      <li>
        <svg viewBox="0 0 12 12"><path d="M3 1 L5 3.5 L4 5 Q5 7 7 8 L8.5 7 L11 9 L9.5 11 Q5 11 1 5 Q1 2 3 1 Z"/></svg>
        <span>310 555 0192</span>
      </li>
      <li>
        <svg viewBox="0 0 12 12"><path d="M1 3 H11 V10 H1 Z M1.5 3.5 L6 7 L10.5 3.5" stroke="#f7f7f5" stroke-width="0.8"/></svg>
        <span>derek@amberridgeassociates.com</span>
      </li>
    </ul>
  </section>
</body>
</html>
```